Brightwell is a company offering Colon Hydrotherapy (or colonics)

Brightwell offers Colon Hydrotherapy using an innovative FDA approved system from the USA. The system is called the TORVA system. The clinic is based in Whangarei, Northland and is the first business of this kind for Northland.
I used to use a design from the Prontaleaf website - a water symbol. However, I want a design that will convey freshness. I want something new and clean which conveys vitality and revitalisation .... perhaps water or bubbles but which brings across the idea of detoxing (which is what colon hydrotherapy does)
The clinic will only be completed in April so for now I have put my mobile number but once in the clinic this will need to be changed to a landline number ... the email address will also change. Thanks for any ideas you give me,
Updates

Hi. I need the name Brightwell first and foremost as this is the name of the Company Underneath this it has to say Colon Hydrotherapy to let people know what Brightwell is My name underneath that would be Marian Holcombe And all contact details to follow this. Thanks !

Target Market(s)

People who are wanting to "detox" and focusing on their health and wellbeing

Industry/Entity Type

Clinic

Contact Information for Business Card

Brightwell
Colon Hydrotherapy
Marian Holcombe
Unit B, 42c Ferrand Lane, Whangarei

021 0487 3916
brightwellclinic@mailnest.example

Font styles to use
Serif

Colors
cee9f6
33a6d7
86cae6

Requirements
Must have
• Stand out with colour or logo

```html
<!DOCTYPE html>
<html lang="en">
<head>
<meta charset="utf-8">
<title>Brightwell – Business Card</title>
<link rel="stylesheet" href="https://fonts.googleapis.com/css2?family=Open+Sans:wght@300;400;700&family=Quicksand:wght@400&display=swap">
<style>
  :root {
    --page-bg: #e9eaeb;
    --card-white: #ffffff;
    --brand-blue: #33a6d7;
    --sky-light: #86cae6;
    --sky-top: #5fc3ef;
    --deep-blue: #2577c2;
    --divider-grey: #8e8e8e;
    --subtitle-grey: #6f6f6f;
    --text-white: #ffffff;
  }
  html, body {
    margin: 0;
    padding: 0;
    width: 1200px;
    height: 900px;
    overflow: hidden;
    background: var(--page-bg);
  }
  .business-card {
    position: absolute;
    left: 180px;
    top: 210px;
    width: 840px;
    height: 480px;
    border-radius: 36px;
    overflow: hidden;
    background: var(--card-white);
    box-shadow: 0 18px 40px rgba(0,0,0,0.18);
  }
  .card-wave {
    position: absolute;
    inset: 0;
    width: 840px;
    height: 480px;
  }
  .brand-block {
    position: absolute;
    top: 34px;
    left: 0;
    width: 100%;
    text-align: center;
  }
  .brand-dot {
    display: block;
    width: 58px;
    height: 58px;
    margin: 0 auto 4px;
    border-radius: 50%;
    background: var(--sky-light);
  }
  .brand-name {
    margin: 0;
    font-family: "Open Sans", sans-serif;
    font-weight: 300;
    font-size: 92px;
    line-height: 1;
    letter-spacing: 1px;
    color: var(--brand-blue);
  }
  .brand-service {
    margin: 6px 0 0 60px;
    font-family: "Quicksand", sans-serif;
    font-size: 20px;
    color: var(--subtitle-grey);
    letter-spacing: 0.5px;
  }
  .contact-block {
    position: absolute;
    top: 300px;
    left: 0;
    width: 100%;
    text-align: center;
    color: var(--text-white);
    font-family: "Open Sans", sans-serif;
  }
  .contact-name {
    margin: 0 0 8px;
    font-weight: 700;
    font-size: 31px;
    line-height: 1.2;
  }
  .contact-line {
    margin: 0;
    font-weight: 400;
    font-size: 25px;
    line-height: 1.42;
  }
</style>
</head>
<body>
  <main class="business-card">
    <svg class="card-wave" viewBox="0 0 840 480" aria-hidden="true">
      <defs>
        <linearGradient id="waveFill" x1="0" y1="0" x2="0" y2="1">
          <stop offset="0" stop-color="var(--sky-top)"/>
          <stop offset="1" stop-color="var(--deep-blue)"/>
        </linearGradient>
      </defs>
      <path d="M0,225 Q420,330 840,190 L840,480 L0,480 Z" fill="url(#waveFill)"/>
      <path d="M0,225 Q420,330 840,190" fill="none" stroke="var(--divider-grey)" stroke-width="3"/>
    </svg>

    <header class="brand-block">
      <span class="brand-dot"></span>
      <h1 class="brand-name">Brightwell</h1>
      <p class="brand-service">Colon Hydrotherapy</p>
    </header>

    <section class="contact-block">
      <h2 class="contact-name">Marian Holcombe</h2>
      <p class="contact-line">021 0487 3916</p>
      <p class="contact-line">brightwellclinic@mailnest.example</p>
      <p class="contact-line">Unit B, 42c Ferrand Lane, Whangarei</p>
    </section>
  </main>
</body>
</html>
```